Bref créative
Business Cards and Stationery for The Cheerful Parcel
The Cheerful Parcel
Traditional
Nora Whitcomb
Chief Executive Officer
24817 Halvern
Dunmore, MI 4735-1186
nora@thecheerfulparcel.example
www.thecheerfulparcel.example
This is my logo in AI

```html
<!DOCTYPE html>
<html lang="en">
<head>
<meta charset="utf-8">
<title>The Cheerful Parcel — Business Card</title>
<link href="https://fonts.googleapis.com/css2?family=Open+Sans:wght@400;600;700&display=swap" rel="stylesheet">
<style>
  :root{
    --bg:#e4e4e6;
    --plum:#6a1f6d;
    --blush:#f3b7c5;
    --blush-soft:#f8d9e1;
    --paper:#ffffff;
    --ink-light:#ffffff;
  }
  *{box-sizing:border-box;margin:0;padding:0}
  html,body{width:1200px;height:895px;overflow:hidden;background:var(--bg);font-family:'Open Sans',Arial,sans-serif}
  .canvas{position:relative;width:1200px;height:895px}
  .card{position:absolute;width:660px;height:377px;background:var(--paper);overflow:hidden;box-shadow:0 6px 18px rgba(0,0,0,.12)}
  .card--front{left:70px;top:50px}
  .card--back{left:470px;top:468px}

  .front-panel{position:absolute;inset:0;width:100%;height:100%}
  .contact{position:absolute;left:34px;top:46px;color:var(--ink-light)}
  .contact__name{font-size:19px;font-weight:700;letter-spacing:.2px}
  .contact__title{font-size:12px;margin-top:2px;opacity:.95}
  .contact__list{list-style:none;margin-top:26px}
  .contact__item{display:flex;align-items:center;gap:8px;font-size:12px;line-height:1.25;margin-bottom:7px}
  .contact__icon{flex:0 0 15px;width:15px;height:15px}

  .brand{position:absolute;left:350px;top:150px;width:290px;text-align:center}
  .brand__mark{display:flex;align-items:center;justify-content:center;gap:10px;white-space:nowrap}
  .brand__dot{flex:0 0 18px;width:18px;height:18px;border-radius:50%;background:var(--blush)}
  .brand__name{font-size:24px;font-weight:700;color:var(--plum);line-height:1.1}
  .brand__tagline{margin-top:14px;font-size:16px;font-weight:600;color:var(--blush)}

  .back-brand{position:absolute;left:0;right:0;top:150px;display:flex;align-items:center;justify-content:center;gap:10px}
  .back-web{position:absolute;left:60px;top:50%;transform:translate(-50%,-50%) rotate(-90deg);font-size:13px;font-weight:600;letter-spacing:2px;color:var(--plum);white-space:nowrap}
</style>
</head>
<body>
<main class="canvas">

  <section class="card card--front" aria-label="Business card front">
    <svg class="front-panel" viewBox="0 0 660 377" aria-hidden="true">
      <path d="M0 0 H300 C236 110 236 262 300 377 H0 Z" fill="var(--plum)"/>
      <path d="M300 0 C236 110 236 262 300 377 H318 C256 262 256 110 318 0 Z" fill="var(--blush-soft)"/>
      <path d="M318 0 C256 110 256 262 318 377" fill="none" stroke="var(--blush)" stroke-width="3"/>
    </svg>

    <div class="contact">
      <p class="contact__name">Nora Whitcomb</p>
      <p class="contact__title">Chief Executive Officer</p>
      <ul class="contact__list">
        <li class="contact__item">
          <svg class="contact__icon" viewBox="0 0 16 16"><circle cx="8" cy="8" r="8" fill="#fff"/><path d="M8 3.5a2.8 2.8 0 0 0-2.8 2.8C5.2 8.4 8 12.5 8 12.5s2.8-4.1 2.8-6.2A2.8 2.8 0 0 0 8 3.5z" fill="var(--plum)"/></svg>
          <span>24817 Halvern<br>Dunmore, MI 4735-1186</span>
        </li>
        <li class="contact__item">
          <svg class="contact__icon" viewBox="0 0 16 16"><circle cx="8" cy="8" r="8" fill="#fff"/><path d="M5 4l2 1.6-1 1.4a6 6 0 0 0 3 3l1.4-1L12 11l-1.2 1.3C7.6 12 4 8.4 3.7 5.2z" fill="var(--plum)"/></svg>
          <span>734-555-0142</span>
        </li>
        <li class="contact__item">
          <svg class="contact__icon" viewBox="0 0 16 16"><circle cx="8" cy="8" r="8" fill="#fff"/><rect x="5" y="4" width="6" height="8" rx="1" fill="var(--plum)"/></svg>
          <span>313-555-0186</span>
        </li>
        <li class="contact__item">
          <svg class="contact__icon" viewBox="0 0 16 16"><circle cx="8" cy="8" r="8" fill="#fff"/><rect x="4" y="5" width="8" height="6" rx="1" fill="var(--plum)"/></svg>
          <span>248-555-0173</span>
        </li>
        <li class="contact__item">
          <svg class="contact__icon" viewBox="0 0 16 16"><circle cx="8" cy="8" r="8" fill="#fff"/><circle cx="8" cy="8" r="3.2" fill="var(--plum)"/></svg>
          <span>mjdowell</span>
        </li>
        <li class="contact__item">
          <svg class="contact__icon" viewBox="0 0 16 16"><circle cx="8" cy="8" r="8" fill="#fff"/><path d="M4 5h8v6H4z M4 5l4 3.2L12 5" fill="none" stroke="var(--plum)" stroke-width="1.2"/></svg>
          <span>nora@thecheerfulparcel.example</span>
        </li>
        <li class="contact__item">
          <svg class="contact__icon" viewBox="0 0 16 16"><circle cx="8" cy="8" r="8" fill="#fff"/><circle cx="8" cy="8" r="3.6" fill="none" stroke="var(--plum)" stroke-width="1.2"/><path d="M4.4 8h7.2" stroke="var(--plum)" stroke-width="1.2"/></svg>
          <span>www.thecheerfulparcel.example</span>
        </li>
      </ul>
    </div>

    <div class="brand">
      <div class="brand__mark">
        <span class="brand__dot"></span>
        <span class="brand__name">The Cheerful Parcel</span>
      </div>
      <p class="brand__tagline">Uplifting gifts for women</p>
    </div>
  </section>

  <section class="card card--back" aria-label="Business card back">
    <p class="back-web">www.thecheerfulparcel.example</p>
    <div class="back-brand">
      <span class="brand__dot"></span>
      <span class="brand__name">The Cheerful Parcel</span>
    </div>
  </section>

</main>
</body>
</html>
```